Gentle Willow Pregnancy and Baby Massage

I need a web design for a new business, GENTLE WILLOW PREGNANCY AND BABY MASSAGE that I am in the process of setting up in the suburbs of Perth, Western Australia. The business is owned and operated by myself and my intention is to service Pregnant Mothers and Parents of Young Babies that would benefit from massage. I would like to have a "Home Page" and pages for "About Me", "Pregnancy Massage", "Baby Massage", a Pricing Page for Pregnancy Massage Sessions, a Pricing Page for Baby Massage Sessions, and a "Contact Me" page to allow clients to either contact me with queries or book available pregnancy massage sessions on a particular day of the week. I would also like a "News" page that would include articles I have written, news about new courses and a link to my Chatterlane page (yet to be set up). I would like to keep the colour schemes similar to my logo design colours. I need the design to be easy to follow and to appeal to a younger audience (20's to mid 30's).
The target audience is pregnant mothers-to-be wishing to receive massage treatments, and new parents and grandparents of small babies that would like to learn how to massage their babies.
The look and feel should be modern, professional, elegant and feminine.
I need the design to be in a standard format such that I can update the content by myself ( and does not need specialised software) as the company and business progresses.

Target Market(s)

Industry/Entity Type

Health And Wellness

Contact Information for Business Card

Card should have rounded edges. Design should have the same "feel" as the website. Contact Details of my business address, mobile phone, email and website should be included.

Coding

Coded - Design and coding required

Number of Pages Required

5+ page

Font styles to use
Script

Requirements
Must have
• Same colours as logo design. In cmyk system, the colours are: 20,60,0,0 which best result is tintora 681 and 40,40,0,0 which best result is tintora 2645. Card should include the logo design.

```html
<!DOCTYPE html>
<html lang="en">
<head>
<meta charset="utf-8">
<title>Gentle Willow Pregnancy and Baby Massage</title>
<link href="https://fonts.googleapis.com/css2?family=Kaushan+Script&family=Open+Sans:ital,wght@0,400;0,600;0,700;1,400&display=swap" rel="stylesheet">
<style>
:root{
  --pink:#b5579d;
  --pink-dark:#9c4586;
  --pink-soft:#f6e6f1;
  --purple:#9784bf;
  --purple-dark:#7d69a8;
  --purple-light:#b8a9d6;
  --ink:#5a5a5a;
  --grey:#8a8a8a;
  --field:#ececec;
  --white:#ffffff;
  --script:"Kaushan Script",cursive;
  --sans:"Open Sans",sans-serif;
}
*{box-sizing:border-box;margin:0;padding:0}
html,body{width:1200px;height:4433px;overflow:hidden}
body{font-family:var(--sans);color:var(--ink);background:var(--white);position:relative}
section,header,footer,nav{position:relative;width:1200px;overflow:hidden}
.abs{position:absolute}
.script{font-family:var(--script);font-weight:400}
.btn{position:absolute;display:flex;align-items:center;justify-content:space-between;background:var(--pink);color:var(--white);border-radius:40px;font-weight:700;font-size:19px;letter-spacing:.5px;padding:0 8px 0 34px}
.btn .dot{width:46px;height:46px;border-radius:50%;background:var(--white);display:block}
.btn.small .dot{width:38px;height:38px}
.photo{position:absolute}

/* header */
.site-header{height:118px}
.brand{left:70px;top:22px;display:flex;align-items:center;gap:14px}
.brand .mark{width:58px;height:58px;border-radius:50%;background:var(--pink-soft);border:3px solid var(--pink)}
.brand .name{font-family:var(--script);color:var(--pink);font-size:20px;line-height:1.15;width:230px}
.call{left:660px;top:28px;display:flex;align-items:center;gap:12px;white-space:nowrap}
.call small{display:block;font-family:var(--script);font-size:13px;color:var(--ink)}
.call strong{display:block;font-size:24px;color:var(--pink);font-weight:600;letter-spacing:.5px}
.site-header .btn{left:890px;top:26px;width:250px;height:62px;font-size:22px}

/* nav */
.main-nav{height:53px;background:var(--white)}
.main-nav ul{position:absolute;left:290px;top:0;width:910px;height:53px;background:var(--purple);display:flex;list-style:none;padding-left:8px}
.main-nav li{color:var(--white);font-size:15px;padding:0 17px;display:flex;align-items:center}
.main-nav li.active{background:var(--purple-light)}

/* hero */
.hero{height:524px}
.hero .photo{inset:0;background:linear-gradient(100deg,#f3ece8 0%,#e9d9d0 30%,#d9b8a6 55%,#efe6e2 80%,#f7f3f1 100%)}
.hero .tag{right:70px;text-align:right;white-space:nowrap}
.hero .t1{top:130px;font-size:50px;color:var(--pink)}
.hero .t2{top:188px;font-size:48px;color:var(--white);text-shadow:0 2px 6px rgba(0,0,0,.25)}
.hero .t3{top:246px;font-size:48px;color:var(--white);text-shadow:0 2px 6px rgba(0,0,0,.25)}
.hero .btn{right:70px;top:320px;width:235px;height:58px}
.hero .dots{right:12px;top:190px;display:flex;flex-direction:column;gap:14px}
.hero .dots i{display:block;width:14px;height:14px;border-radius:50%;border:2px solid var(--white)}
.hero .dots i.on{background:var(--white)}

/* newsletter */
.newsletter{height:103px;background:var(--purple)}
.newsletter .ask{left:0;top:0;width:760px;height:103px}
.newsletter .ask p{position:absolute;left:80px;top:24px;width:560px;font-style:italic;color:var(--white);font-size:17px;line-height:1.5}
.newsletter .mail{left:740px;top:28px;display:flex;align-items:center;gap:16px;color:var(--white);font-size:17px}

/* welcome */
.welcome{height:452px;text-align:center}
.welcome h1{position:absolute;top:58px;width:100%;font-size:42px;color:var(--pink)}
.welcome .sub{position:absolute;top:122px;width:100%;color:var(--purple);font-size:19px}
.welcome .copy{position:absolute;left:150px;top:168px;width:900px;font-size:14.5px;line-height:1.75;color:var(--ink)}
.welcome .copy p+p{margin-top:10px}
.welcome .btn{left:486px;top:334px;width:228px;height:58px}

/* strip */
.strip{height:340px}
.strip .left{left:0;top:0;width:390px;height:340px;background:linear-gradient(135deg,#e2b5a6,#c98c80 50%,#b0776d)}
.strip .right{left:800px;top:0;width:400px;height:340px;background:linear-gradient(135deg,#b59a8e,#8c6b5f 50%,#a3897e)}
.strip .panel{left:410px;top:0;width:380px;height:340px;background:var(--purple)}
.strip .panel .frame{position:absolute;left:18px;top:18px;right:18px;bottom:18px;border:2px solid var(--purple-light)}
.strip .panel .emblem{position:absolute;left:158px;top:58px;width:64px;height:64px;border-radius:50%;border:4px solid var(--white)}
.strip .panel p{position:absolute;left:50px;top:148px;width:280px;text-align:center;color:var(--white);font-style:italic;font-size:15px;line-height:1.6}

/* service blocks */
.service{height:500px}
.service .glow{position:absolute;border-radius:50%;background:radial-gradient(circle,var(--pink-soft) 55%,rgba(246,230,241,0) 72%)}
.service .circle{position:absolute;width:360px;height:360px;border-radius:50%;border:10px solid var(--white);box-shadow:0 0 0 2px var(--pink-soft)}
.service h2{position:absolute;font-size:36px;color:var(--pink)}
.service .lead{position:absolute;color:var(--purple);font-style:italic;font-size:15px;line-height:1.6}
.service h3{position:absolute;font-family:var(--script);font-weight:400;font-size:22px;color:var(--ink);line-height:1.3}
.service ul{position:absolute;list-style:none;font-size:14.5px;line-height:1.55;color:var(--ink)}
.service li{display:flex;gap:12px;margin-bottom:8px}
.service li svg{flex:none;margin-top:3px}
.service .btn{width:228px;height:58px}

.pregnancy .glow{left:60px;top:20px;width:460px;height:460px}
.pregnancy .circle{left:110px;top:70px;background:linear-gradient(135deg,#f0e6e2,#d8c2b8 60%,#c7a697)}
.pregnancy h2{left:608px;top:40px}
.pregnancy .lead{left:608px;top:100px;width:520px}
.pregnancy h3{left:608px;top:168px;width:470px}
.pregnancy ul{left:608px;top:240px;width:520px}
.pregnancy .btn{left:600px;top:406px}

.baby{height:510px}
.baby .glow{left:660px;top:20px;width:460px;height:460px}
.baby .circle{left:700px;top:60px;background:linear-gradient(135deg,#f4e1d6,#e0b9a4 60%,#c99a85)}
.baby h2{left:80px;top:40px}
.baby .lead{left:80px;top:100px;width:540px}
.baby h3{left:80px;top:186px}
.baby ul{left:80px;top:232px;width:560px}
.baby .btn{left:80px;top:400px}

/* price */
.price{height:640px}
.price .photo{inset:0;background:linear-gradient(135deg,#a38fc8,#8e79b6 45%,#a695cc 75%,#c2b4dc)}
.price h2{position:absolute;top:58px;width:100%;text-align:center;font-size:40px;color:var(--white)}
.price .sub{position:absolute;top:115px;left:300px;width:600px;text-align:center;color:var(--white);font-style:italic;font-size:16px;line-height:1.55}
.tabs{position:absolute;top:178px;left:0;width:100%;display:flex;justify-content:center;gap:18px}
.tabs span{display:block;padding:14px 30px;border-radius:40px;border:2px solid var(--white);color:var(--white);font-size:17px}
.tabs span.on{background:var(--pink);border-color:var(--pink-soft)}
.price-card{position:absolute;left:80px;top:262px;width:308px;height:312px;background:var(--white);border-radius:6px;text-align:center;box-shadow:0 4px 14px rgba(0,0,0,.15)}
.price-card h4{margin:26px 30px 0;padding-bottom:14px;font-family:var(--script);font-weight:400;color:var(--pink);font-size:22px;line-height:1.2;border-bottom:1px solid #ddd}
.price-card .label{margin-top:14px;color:var(--pink);font-size:15px;text-decoration:underline}
.price-card .val{margin-top:4px;font-size:16px;color:var(--ink)}
.price-card .btn{left:62px;top:238px;width:190px;height:52px;font-size:17px;padding-left:26px}
.course{position:absolute;top:295px;width:220px;text-align:center;color:var(--white);font-size:18px;line-height:1.45}
.course i{display:block;margin:0 auto 22px;width:112px;height:112px;border-radius:50%;border:6px solid var(--white)}

/* testimonials */
.testimonials{height:272px;background:var(--pink)}
.testimonials h2{position:absolute;left:130px;top:92px;font-size:40px;color:var(--white)}
.testimonials .who{position:absolute;left:146px;top:148px;color:var(--white);font-size:16px}
.testimonials .rule{position:absolute;left:392px;top:40px;width:2px;height:190px;background:rgba(255,255,255,.6)}
.testimonials .avatar{position:absolute;left:440px;top:40px;width:130px;height:130px;border-radius:50%;border:5px solid var(--white);background:linear-gradient(135deg,#d8b9a8,#a87d6b)}
.testimonials blockquote{position:absolute;left:600px;top:44px;width:540px;color:var(--white);font-style:italic;font-size:16px;line-height:1.7}
.testimonials cite{position:absolute;left:890px;top:148px;font-family:var(--script);font-style:normal;color:var(--white);font-size:20px}
.testimonials .dots{position:absolute;left:540px;top:226px;display:flex;gap:10px}
.testimonials .dots i{width:14px;height:14px;border-radius:50%;border:2px solid var(--white)}
.testimonials .dots i.on{background:var(--white)}

/* contact */
.contact{height:561px}
.contact h2{position:absolute;left:80px;top:56px;font-size:40px;color:var(--pink)}
.contact .sub{position:absolute;left:80px;top:118px;font-style:italic;font-size:17px;color:var(--ink)}
.contact form{position:absolute;left:80px;top:160px;width:500px}
.contact .field{height:44px;background:var(--field);margin-bottom:9px;padding:12px 14px;font-size:13px;color:var(--grey)}
.contact .field.area{height:120px}
.contact .btn{left:80px;top:438px;width:190px;height:56px;font-size:20px;padding-left:30px}
.contact .photo{left:700px;top:0;width:500px;height:561px;background:linear-gradient(160deg,#ffffff 0%,#f3e7e2 35%,#e2c2b2 65%,#d4a794 100%)}

/* footer */
.site-footer{height:297px;background:var(--pink)}
.site-footer h5{position:absolute;top:36px;color:var(--white);font-size:16px;font-weight:700;letter-spacing:.5px}
.sitemap{position:absolute;left:80px;top:76px;list-style:none;color:var(--white);font-size:14px;line-height:1.6}
.sitemap li::before{content:"";display:inline-block;width:8px;height:8px;border-radius:50%;background:var(--white);margin:0 16px 1px 0}
.fcontact{position:absolute;left:340px;top:76px;width:240px;color:var(--white);font-size:14px;line-height:1.5}
.fcontact .row{display:flex;gap:14px;margin-bottom:16px}
.fcontact .row svg{flex:none;margin-top:2px}
.news{position:absolute;left:606px;top:76px;width:270px;color:var(--white);font-size:14px;line-height:1.45}
.news .item{display:flex;gap:14px;margin-bottom:22px}
.news .thumb{flex:none;width:66px;height:66px;border-radius:50%;background:linear-gradient(135deg,#e9c9b8,#b88b78)}
.news .date{display:flex;gap:8px;align-items:center;margin-top:4px}
.badge{position:absolute;left:895px;top:80px;width:230px;height:130px;background:var(--white);display:flex;align-items:center;justify-content:center}
.badge i{width:84px;height:84px;border-radius:50%;background:var(--purple-light)}
.social{position:absolute;left:960px;top:232px;color:var(--white);font-size:15px;font-weight:600}
.copyright{height:63px;background:var(--purple);color:var(--white);font-size:14px;display:flex;align-items:center;justify-content:center}
</style>
</head>
<body>

<header class="site-header">
  <div class="brand abs">
    <span class="mark"></span>
    <span class="name">Gentle Willow Pregnancy and Baby Massage</span>
  </div>
  <div class="call abs">
    <svg width="34" height="34" viewBox="0 0 24 24" aria-hidden="true"><path fill="#b5579d" d="M6.6 10.8a15.1 15.1 0 0 0 6.6 6.6l2.2-2.2a1 1 0 0 1 1-.25 11.4 11.4 0 0 0 3.6.57 1 1 0 0 1 1 1V20a1 1 0 0 1-1 1A17 17 0 0 1 3 4a1 1 0 0 1 1-1h3.5a1 1 0 0 1 1 1c0 1.25.2 2.45.57 3.6a1 1 0 0 1-.25 1z"/></svg>
    <div><small>Call Us Today -</small><strong>040 0555 190</strong></div>
  </div>
  <a class="btn">BOOK NOW <span class="dot"></span></a>
</header>

<nav class="main-nav">
  <ul>
    <li>HOME</li><li class="active">ABOUT ME</li><li>PREGNANCY MASSAGE</li><li>BABY MASSAGE</li><li>PRICE</li><li>NEWS</li><li>CONTACT US</li>
  </ul>
</nav>

<section class="hero">
  <div class="photo" role="img" aria-label="Photo of a pregnant woman relaxing on a white bed while receiving a belly massage"></div>
  <div class="tag abs t1 script">It's All About You</div>
  <div class="tag abs t2 script">Gentle Willow pregnancy And</div>
  <div class="tag abs t3 script">Baby Massage</div>
  <a class="btn">BOOK NOW <span class="dot"></span></a>
  <div class="dots abs"><i class="on"></i><i></i><i></i><i></i></div>
</section>

<section class="newsletter">
  <svg class="ask abs" viewBox="0 0 760 103" aria-hidden="true"><polygon points="0,0 710,0 760,51 710,103 0,103" fill="#b5579d"/></svg>
  <div class="ask abs">
    <p>Would you like to receive exclusive access to articles, white papers and our regular monthly newsletter?</p>
    <svg class="abs" style="left:640px;top:32px" width="40" height="40" viewBox="0 0 24 24" aria-hidden="true"><path fill="none" stroke="#fff" stroke-width="1.6" stroke-linejoin="round" d="M22 2 2 10l8 3 3 8z M22 2 10 13"/></svg>
  </div>
  <div class="mail abs">
    <svg width="44" height="34" viewBox="0 0 44 34" aria-hidden="true"><rect x="2" y="2" width="40" height="30" rx="2" fill="none" stroke="#fff" stroke-width="2.5"/><path d="M2 4l20 15L42 4" fill="none" stroke="#fff" stroke-width="2.5"/></svg>
    maren@gentlewillow-massage.example
  </div>
</section>

<section class="welcome">
  <h1 class="script">Welcome To Gentle Willow</h1>
  <div class="sub">Pregnancy And Baby Massage</div>
  <div class="copy">
    <p>Maren is a Practitioner of Pregnancy Massage, and a Paediatric Massage Consultant. She completed her training with Prenatal Touch Network, and the Infant Touch Resource Service. The ITRS is endorsed by the Coastal College of Midwifery. The Natural Therapies Guild, and accredited by the Guild of Bodywork Therapists.</p>
    <p>Maren is also a Registered Nurse and Midwife. Most of her professional career has been as a midwife, which has included working in the community in the UK, providing ante natal care and classes, intra partum care, home births, and postnatal care in the home. Maren has also worked in the private and public maternity sectors in Perth.</p>
  </div>
  <a class="btn">LEARN MORE <span class="dot"></span></a>
</section>

<section class="strip">
  <div class="photo left" role="img" aria-label="Photo of two newborn twins sleeping on a soft blanket"></div>
  <div class="panel abs">
    <svg class="abs" style="left:-22px;top:150px" width="24" height="40" viewBox="0 0 24 40" aria-hidden="true"><polygon points="24,0 0,20 24,40" fill="#9784bf"/></svg>
    <div class="frame"></div>
    <span class="emblem"></span>
    <p>Gentle Willow Pregnancy and Baby Massage was launched in 2017, offering massage for pregnant women, and instruction of baby massage to parents, grandparents and carers.</p>
  </div>
  <div class="photo right" role="img" aria-label="Photo of newborn twins curled together in a basket"></div>
</section>

<section class="service pregnancy">
  <div class="glow"></div>
  <div class="circle" role="img" aria-label="Photo of hands gently massaging a pregnant belly"></div>
  <h2 class="script">Pregnancy Massage</h2>
  <p class="lead">Pregnancy massage is the prenatal use of massage therapy to support the physiological, structural and emotional wellbeing of both mother and baby.</p>
  <h3>Pregnancy Massage is a professional relaxation massage</h3>
  <ul>
    <li><svg width="16" height="16" viewBox="0 0 16 16" aria-hidden="true"><path d="M2 8l4 4 8-9" fill="none" stroke="#b5579d" stroke-width="2.4"/></svg>Reduces anxiety caused by hormonal changes</li>
    <li><svg width="16" height="16" viewBox="0 0 16 16" aria-hidden="true"><path d="M2 8l4 4 8-9" fill="none" stroke="#b5579d" stroke-width="2.4"/></svg>Improves circulation</li>
    <li><svg width="16" height="16" viewBox="0 0 16 16" aria-hidden="true"><path d="M2 8l4 4 8-9" fill="none" stroke="#b5579d" stroke-width="2.4"/></svg>Reduces muscle aches and pain; muscle and joint conditions such as backache, shoulder and neck pain, hip pain, leg cramps, oedema and carpal tunnel</li>
  </ul>
  <a class="btn">LEARN MORE <span class="dot"></span></a>
</section>

<section class="service baby">
  <div class="glow"></div>
  <div class="circle" role="img" aria-label="Photo of an adult hand holding tiny baby feet"></div>
  <h2 class="script">Baby Massage</h2>
  <p class="lead">Baby massage was first described in China circa 4000 years ago, then in India and Egypt, and was passed down from mother to daughter over the generations.</p>
  <h3>Benefits of Baby massage</h3>
  <ul>
    <li><svg width="16" height="16" viewBox="0 0 16 16" aria-hidden="true"><path d="M2 8l4 4 8-9" fill="none" stroke="#b5579d" stroke-width="2.4"/></svg>Relaxation of skeletal muscles</li>
    <li><svg width="16" height="16" viewBox="0 0 16 16" aria-hidden="true"><path d="M2 8l4 4 8-9" fill="none" stroke="#b5579d" stroke-width="2.4"/></svg>Strengthens the immune system</li>
    <li><svg width="16" height="16" viewBox="0 0 16 16" aria-hidden="true"><path d="M2 8l4 4 8-9" fill="none" stroke="#b5579d" stroke-width="2.4"/></svg>Reduces stress hormone levels in children and parents</li>
    <li><svg width="16" height="16" viewBox="0 0 16 16" aria-hidden="true"><path d="M2 8l4 4 8-9" fill="none" stroke="#b5579d" stroke-width="2.4"/></svg>Improves sleep and regulates sleep patterns</li>
    <li><svg width="16" height="16" viewBox="0 0 16 16" aria-hidden="true"><path d="M2 8l4 4 8-9" fill="none" stroke="#b5579d" stroke-width="2.4"/></svg>Relieves discomfort of wind, constipation, colic and reflux</li>
  </ul>
  <a class="btn">LEARN MORE <span class="dot"></span></a>
</section>

<section class="price">
  <div class="photo" role="img" aria-label="Soft lilac-tinted photo of a mother with her baby"></div>
  <h2 class="script">Our Price</h2>
  <p class="sub">Contact Me With Queries Or Book Available Pregnancy Massage Sessions On A Particular Day Of The Week.</p>
  <div class="tabs"><span>Pregnancy Massage Sessions</span><span class="on">Baby Massage Sessions</span></div>
  <div class="price-card">
    <h4>Basic Massage Techniques</h4>
    <div class="label">Duration</div>
    <div class="val">75 mins session</div>
    <div class="label">Cost</div>
    <div class="val">$115 - including 15 mins consultation.</div>
    <a class="btn small">BOOK NOW <span class="dot"></span></a>
  </div>
  <div class="course" style="left:440px"><i></i>Colic Relief<br>Course</div>
  <div class="course" style="left:700px"><i></i>Ante Natal<br>Session</div>
  <div class="course" style="left:960px"><i></i>Advanced Baby<br>Massage</div>
</section>

<section class="testimonials">
  <h2 class="script">Testimonials</h2>
  <div class="who">What Our Client Say</div>
  <div class="rule"></div>
  <div class="avatar" role="img" aria-label="Client portrait photo"></div>
  <blockquote>" Lorem Ipsum is simply dummy text of the printing and typesetting industry. Lorem Ipsum has been the industry's standard dummy text ever since the 1500s, when an unknown printer took a galley of type "</blockquote>
  <cite>— Tessa Lindqvist</cite>
  <div class="dots"><i></i><i class="on"></i><i></i><i></i><i></i></div>
</section>

<section class="contact">
  <h2 class="script">Contact Us</h2>
  <p class="sub">Need a free quote, or have a question? Get in touch!</p>
  <form>
    <div class="field">Name*</div>
    <div class="field">Email*</div>
    <div class="field">Phone*</div>
    <div class="field area">Message*</div>
  </form>
  <a class="btn">SUBMIT <span class="dot"></span></a>
  <div class="photo" role="img" aria-label="Photo of a pregnant belly with hands holding a red paper heart"></div>
</section>

<footer class="site-footer">
  <h5 style="left:80px">SITEMAP</h5>
  <ul class="sitemap">
    <li>Home</li><li>About Me</li><li>Pregnancy Massage</li><li>Baby Massage</li><li>Price</li><li>News</li><li>Contact Us</li>
  </ul>
  <h5 style="left:340px">CONTACT US</h5>
  <div class="fcontact">
    <div class="row"><svg width="18" height="24" viewBox="0 0 18 24" aria-hidden="true"><path fill="#fff" d="M9 0a9 9 0 0 0-9 9c0 7 9 15 9 15s9-8 9-15a9 9 0 0 0-9-9zm0 12.5A3.5 3.5 0 1 1 9 5.5a3.5 3.5 0 0 1 0 7z"/></svg><div>Gentle Willow Pregnancy and Infant Massage<br>Maren Holloway</div></div>
    <div class="row"><svg width="18" height="18" viewBox="0 0 24 24" aria-hidden="true"><path fill="#fff" d="M6.6 10.8a15.1 15.1 0 0 0 6.6 6.6l2.2-2.2a1 1 0 0 1 1-.25 11.4 11.4 0 0 0 3.6.57 1 1 0 0 1 1 1V20a1 1 0 0 1-1 1A17 17 0 0 1 3 4a1 1 0 0 1 1-1h3.5a1 1 0 0 1 1 1c0 1.25.2 2.45.57 3.6a1 1 0 0 1-.25 1z"/></svg><div>040 0555 190</div></div>
    <div class="row"><svg width="18" height="14" viewBox="0 0 18 14" aria-hidden="true"><rect x="1" y="1" width="16" height="12" fill="none" stroke="#fff" stroke-width="1.6"/><path d="M1 2l8 6 8-6" fill="none" stroke="#fff" stroke-width="1.6"/></svg><div>maren@gentlewillow-massage.example</div></div>
  </div>
  <h5 style="left:606px">LATEST NEWS</h5>
  <div class="news">
    <div class="item"><span class="thumb" role="img" aria-label="News thumbnail photo"></span><div>Lorem Ipsum is simple dummy text of print.<div class="date"><svg width="14" height="14" viewBox="0 0 14 14" aria-hidden="true"><rect x="1" y="2" width="12" height="11" fill="none" stroke="#fff" stroke-width="1.4"/><path d="M1 5h12" stroke="#fff" stroke-width="1.4"/></svg>26 Sep 2017</div></div></div>
    <div class="item"><span class="thumb" role="img" aria-label="News thumbnail photo"></span><div>Lorem Ipsum is simple dummy text of print.<div class="date"><svg width="14" height="14" viewBox="0 0 14 14" aria-hidden="true"><rect x="1" y="2" width="12" height="11" fill="none" stroke="#fff" stroke-width="1.4"/><path d="M1 5h12" stroke="#fff" stroke-width="1.4"/></svg>26 Sep 2017</div></div></div>
  </div>
  <div class="badge" role="img" aria-label="Certification badge"><i></i></div>
  <div class="social">Chatterlane</div>
</footer>

<div class="copyright">© Gentle Willow Pregnancy and Infant Massage- 2017 All Right Reserved</div>

</body>
</html>
```